Velmor Agritech, Inc. Business Card

We are joint venture hybrid vegetable seed company. We design & breed application specific products for fresh market and processing applications. We are looking for a business card that will have impact and convey elegance, excellence, high technology, and have enormous eye appeal. It needs to be unique in design and can incorporate photos, or symbols as the case may be.

I very much enjoy the minimalist approach to Quorlin's product designs. We would like to include a tag line in the business card: Breeding Success

Target Market(s)

We breed proprietary products that provide better solutions for growers, harvesters, packers, shippers, wholesalers, retailers, consumers, and processors. Regional seed distributors worldwide are our primary clients and then growers. We need to appeal first and foremost to the distributors who will be representing us and selling the products in their target markets.

Industry/Entity Type

Business

Requirements
Must have
• It will have a picture of a cluster of tomatoes on one side and the other side will include the logo, a tag line, our contact information, and a possibly a picture or symbol. I want the contact side to be edgy and convey elegance, solidity, and exclusivity.
Nice to have
• Surprise us with something special.
Should not have
• Card needs to work well with the green logo so it can't be diminished by the background color of the card.

```html
<!DOCTYPE html>
<html lang="en">
<head>
<meta charset="utf-8">
<title>Velmor Agritech, Inc. Business Card</title>
<link href="https://fonts.googleapis.com/css2?family=Arimo:wght@400;700&display=swap" rel="stylesheet">
<style>
  :root {
    --page: #efece6;
    --card-white: #ffffff;
    --brand-green: #1d6b40;
    --tomato-red: #c42a1e;
    --tomato-deep: #a51c14;
    --vine-green: #7d9a68;
    --leaf-pale: #d3dccb;
    --shadow: rgba(0, 0, 0, 0.18);
  }
  * { box-sizing: border-box; margin: 0; padding: 0; }
  html, body {
    width: 1200px;
    height: 1000px;
    overflow: hidden;
    background: var(--page);
    font-family: "Arimo", Arial, sans-serif;
  }
  .sheet {
    position: relative;
    width: 1200px;
    height: 1000px;
  }
  .card {
    position: absolute;
    left: 280px;
    width: 640px;
    height: 392px;
    overflow: hidden;
    box-shadow: 0 6px 18px var(--shadow);
  }
  .card--front { top: 78px; }
  .card--contact { top: 530px; background: var(--card-white); }

  .photo-tomatoes {
    position: absolute;
    inset: 0;
    background: linear-gradient(115deg, var(--leaf-pale) 0%, var(--vine-green) 22%, var(--tomato-red) 48%, var(--tomato-deep) 72%, var(--vine-green) 100%);
  }
  .url-frame {
    position: absolute;
    left: 50%;
    top: 50%;
    transform: translate(-50%, -50%);
    padding: 10px 24px;
    border: 2px solid var(--card-white);
    color: var(--card-white);
    font-size: 21px;
    letter-spacing: 1.5px;
    white-space: nowrap;
  }

  .contact-shape {
    position: absolute;
    inset: 0;
    width: 640px;
    height: 392px;
  }
  .contact-shape .photo-fill { fill: url(#tomatoTone); }
  .contact-shape .white-panel { fill: var(--card-white); }

  .brand {
    position: absolute;
    right: 56px;
    top: 58px;
    display: flex;
    flex-direction: column;
    align-items: flex-end;
    gap: 8px;
    color: var(--brand-green);
  }
  .brand-row {
    display: flex;
    align-items: center;
    gap: 10px;
  }
  .brand-dot {
    width: 16px;
    height: 16px;
    border-radius: 50%;
    background: var(--brand-green);
  }
  .brand-name {
    font-size: 21px;
    font-weight: 700;
  }
  .brand-tagline {
    font-size: 14px;
    font-weight: 400;
    letter-spacing: 2.5px;
    text-transform: uppercase;
  }
  .contact {
    position: absolute;
    left: 73px;
    top: 146px;
    color: var(--brand-green);
  }
  .contact-name {
    font-size: 21px;
    font-weight: 700;
    letter-spacing: 2px;
    margin-bottom: 14px;
  }
  .contact-line {
    font-size: 18px;
    line-height: 30px;
    letter-spacing: 0.6px;
  }
  .contact-web { margin-top: 12px; }
</style>
</head>
<body>
<main class="sheet">
  <section class="card card--front">
    <div class="photo-tomatoes" role="img" aria-label="Photo of a cluster of ripe red tomatoes on the vine"></div>
    <div class="url-frame">www.velmoragritech.com</div>
  </section>

  <section class="card card--contact">
    <svg class="contact-shape" viewBox="0 0 640 392" role="img" aria-label="Photo of red vine tomatoes showing in the top-left and bottom-right corners">
      <defs>
        <linearGradient id="tomatoTone" x1="0" y1="0" x2="1" y2="1">
          <stop offset="0" stop-color="#c42a1e"/>
          <stop offset="0.5" stop-color="#7d9a68"/>
          <stop offset="1" stop-color="#c42a1e"/>
        </linearGradient>
      </defs>
      <rect class="photo-fill" width="640" height="392"/>
      <path class="white-panel" d="M0,392 L0,200 C0,80 60,0 172,0 L640,0 L640,216 C640,332 562,392 442,392 Z"/>
    </svg>

    <div class="brand">
      <div class="brand-row">
        <span class="brand-dot"></span>
        <span class="brand-name">Velmor Agritech, Inc.</span>
      </div>
      <span class="brand-tagline">Breeding Success</span>
    </div>

    <div class="contact">
      <p class="contact-name">MARA ELLISON</p>
      <p class="contact-line">48 Larchmont Row</p>
      <p class="contact-line">Fairhaven, 2041</p>
      <p class="contact-line">United States</p>
      <p class="contact-line">(555) 218-4470</p>
      <p class="contact-line contact-web">www.velmoragritech.com</p>
    </div>
  </section>
</main>
</body>
</html>
```